"Retire With The Ashbury Trust" Book Cover Design

This book is 5.5 x. 8.5 in size. Not enough room for any writing on the spine either. About 100 pages, and 18,000 words max.
The Ashbury Trust goes back to 1930. In this book, I run scenario after scenario seeing what the best strategy was for someone to Retire With The Ashbury Trust and never run out of money. And how they MIGHT be able to use this info to build a solid retirement plan using the Ashbury Trust for themselves.
Target Market(s)
Soon-to-be and recent middle-class, married retirees.
Industry/Entity Type
Investment Advisory
Requirements
Must have
- MUST BE EYE CATCHING!
Should not have
- No Piggy Banks or old people sitting on a beach or any yachts.

```html
<!DOCTYPE html>
<html lang="en">
<head>
<meta charset="utf-8">
<title>Retire With The Ashbury Trust — Book Cover</title>
<link rel="stylesheet" href="https://fonts.googleapis.com/css2?family=Cinzel:wght@400&family=Open+Sans:wght@400;800&family=Roboto:wght@700&display=swap">
<style>
  :root {
    --paper: #ffffff;
    --ink: #111111;
    --navy: #1f1d86;
    --crimson: #bb101b;
    --nest-dark: #6b5237;
    --nest-mid: #a58a66;
    --nest-light: #e9e0d2;
  }
  html, body {
    margin: 0;
    padding: 0;
    width: 769px;
    height: 1200px;
    overflow: hidden;
    background: var(--paper);
  }
  .cover {
    display: block;
    width: 769px;
    height: 1200px;
  }
  .title-lead {
    font-family: "Open Sans", sans-serif;
    font-weight: 400;
    fill: var(--ink);
  }
  .title-name {
    font-family: "Open Sans", sans-serif;
    font-weight: 800;
    fill: var(--navy);
  }
  .title-key {
    font-family: "Open Sans", sans-serif;
    font-weight: 800;
    fill: var(--crimson);
  }
  .subtitle-frame {
    fill: none;
    stroke: var(--navy);
    stroke-width: 2.5;
  }
  .subtitle {
    font-family: "Roboto", sans-serif;
    font-weight: 700;
    fill: var(--ink);
  }
  .author {
    font-family: "Cinzel", serif;
    font-weight: 400;
    fill: var(--navy);
  }
</style>
</head>
<body>
<svg class="cover" viewBox="0 0 769 1200" xmlns="http://www.w3.org/2000/svg">
  <defs>
    <radialGradient id="nest-tone" cx="0.5" cy="0.62" r="0.55">
      <stop offset="0" stop-color="var(--nest-dark)"/>
      <stop offset="0.45" stop-color="var(--nest-mid)"/>
      <stop offset="0.8" stop-color="var(--nest-light)"/>
      <stop offset="1" stop-color="var(--paper)"/>
    </radialGradient>
  </defs>

  <rect class="cover-paper" x="0" y="0" width="769" height="1200" fill="var(--paper)"/>

  <g class="title">
    <text class="title-lead" x="58" y="147" font-size="85" textLength="651" lengthAdjust="spacingAndGlyphs">RETIRE WITH THE</text>
    <text class="title-name" x="58" y="248" font-size="108" textLength="651" lengthAdjust="spacingAndGlyphs">ASHBURY</text>
    <text class="title-key" x="58" y="453" font-size="215" textLength="651" lengthAdjust="spacingAndGlyphs">TRUST</text>
  </g>

  <g class="subtitle-block">
    <rect class="subtitle-frame" x="58" y="479" width="651" height="109"/>
    <text class="subtitle" x="81" y="527" font-size="29" textLength="617" lengthAdjust="spacingAndGlyphs">BUILD A SOLID RETIREMENT PLAN USING</text>
    <text class="subtitle" x="81" y="567" font-size="29" textLength="617" lengthAdjust="spacingAndGlyphs">THE ASHBURY TRUST FOR THEMSELVES</text>
  </g>

  <rect class="cover-photo" x="123" y="590" width="562" height="455" fill="url(#nest-tone)"
        role="img" aria-label="Photo of a twig bird's nest holding eggs, with a small bird carrying a folded hundred-dollar bill"/>

  <text class="author" x="123" y="1163" font-size="78" textLength="527" lengthAdjust="spacingAndGlyphs">Author Name</text>
</svg>
</body>
</html>
```